DJ-ing Business Card Needed!!

Im an 18 year old DJ, playing house, EDM (electro dance music),
I use social media (facebook, instagram,soundcloud) as my main platforms of advertising.

I have logos and qr codes, as well as a few images of myself djing, that may be useful,

Any other photos you may need/want, check out my facebook page, 'dj Lorcan Beveridge'

Target Market(s)

Range of ages, 16-60

Contact Information for Business Card

Hi All,
My logo, QR code, email, facebook/sound cloud web addresses, mobile number

Logo Text

DJ LORCAN BEVERIDGE

Requirements
Must have
• These links must be on the design:

https://www.pagebook-example.com/DjLorcanBeveridge

Phone number: 0412739264

Email: lorcan.beveridge@mailnest-example.com.au

Nice to have
• https://tuneharbor-example.com/djlorcanbeveridge (the QR code may be sufficient)

The wordmark logo to be white,

```html
<!DOCTYPE html>
<html lang="en">
<head>
<meta charset="utf-8">
<title>DJ Lorcan Beveridge – Business Card</title>
<link rel="stylesheet" href="https://fonts.googleapis.com/css2?family=Open+Sans:wght@300;400;700&display=swap">
<style>
  :root {
    --card-base: #16131d;
    --photo-dark: #1d1b22;
    --photo-mid: #3c3a42;
    --crowd-grey: #6c6672;
    --crowd-purple: #4a3870;
    --crowd-deep: #2a2046;
    --band-dark: rgba(10, 8, 14, 0.55);
    --band-light: rgba(150, 140, 170, 0.12);
    --text-white: #ffffff;
    --text-soft: #f1eef6;
  }
  * { margin: 0; padding: 0; box-sizing: border-box; }
  html, body {
    width: 1200px;
    height: 741px;
    overflow: hidden;
    background: var(--card-base);
  }
  .card {
    position: relative;
    width: 1200px;
    height: 741px;
    overflow: hidden;
    background: var(--card-base);
    font-family: "Open Sans", Arial, sans-serif;
    color: var(--text-white);
  }
  .crowd-scene {
    position: absolute;
    left: 380px; top: 0;
    width: 820px; height: 741px;
    background:
      radial-gradient(ellipse 360px 220px at 75% 28%, rgba(170,150,175,0.55), transparent 70%),
      radial-gradient(ellipse 300px 260px at 88% 88%, rgba(120,50,60,0.45), transparent 70%),
      linear-gradient(160deg, var(--crowd-grey) 0%, var(--crowd-purple) 45%, var(--crowd-deep) 100%);
  }
  .dj-photo {
    position: absolute;
    left: 0; top: 0;
    width: 540px; height: 741px;
    background:
      radial-gradient(ellipse 220px 320px at 35% 50%, var(--photo-mid), transparent 75%),
      linear-gradient(180deg, var(--photo-dark) 0%, #26242b 60%, #1a1820 100%);
    clip-path: polygon(0 0, 440px 0, 540px 741px, 0 741px);
  }
  .bands {
    position: absolute;
    inset: 0;
    width: 1200px;
    height: 741px;
  }
  .handle-top {
    position: absolute;
    left: 292px; top: 128px;
    width: 800px;
    text-align: right;
    font-weight: 300;
    font-size: 20px;
    letter-spacing: 5px;
    color: var(--text-soft);
  }
  .wordmark {
    position: absolute;
    left: 520px; top: 228px;
    width: 580px;
    text-align: center;
    font-weight: 700;
    text-transform: uppercase;
    color: var(--text-white);
    line-height: 1;
  }
  .wordmark .prefix { display: block; font-size: 60px; margin-bottom: 18px; }
  .wordmark .name { display: block; font-size: 74px; margin-bottom: 12px; }
  .contact-line {
    position: absolute;
    left: 523px; top: 535px;
    font-weight: 400;
    font-size: 20px;
    color: var(--text-soft);
    white-space: nowrap;
  }
  .contact-line .divider { margin: 0 10px; }
  .handle-bottom {
    position: absolute;
    left: 523px; top: 587px;
    font-weight: 300;
    font-size: 18px;
    letter-spacing: 3px;
    color: var(--text-soft);
    white-space: nowrap;
  }
</style>
</head>
<body>
<main class="card">
  <div class="crowd-scene" role="img" aria-label="Photo of a festival crowd under stage lights"></div>
  <div class="dj-photo" role="img" aria-label="Photo of the DJ mixing on decks with headphones around his neck"></div>

  <svg class="bands" viewBox="0 0 1200 741" aria-hidden="true">
    <polygon points="0,40 60,0 120,0 0,180" fill="var(--band-light)"/>
    <polygon points="420,0 470,0 620,741 560,741" fill="var(--band-dark)"/>
    <polygon points="720,0 800,0 1140,741 1050,741" fill="var(--band-dark)"/>
    <polygon points="830,0 860,0 1200,640 1200,700" fill="var(--band-light)"/>
    <polygon points="0,560 420,741 300,741 0,620" fill="var(--band-dark)"/>
    <polygon points="140,380 460,300 470,340 150,420" fill="var(--band-light)"/>
  </svg>

  <p class="handle-top">tuneharbor-example.com/djlorcanbeveridge</p>

  <h1 class="wordmark">
    <span class="prefix">DJ</span>
    <span class="name">Lorcan</span>
    <span class="name">Beveridge</span>
  </h1>

  <p class="contact-line">0412739264<span class="divider">I</span>lorcan.beveridge@mailnest-example.com.au</p>
  <p class="handle-bottom">www.pagebook-example.com/djlorcanbeveridge</p>
</main>
</body>
</html>
```